What makes us Different Managed Communications Services Provider Flyer

We need a flyer to explain why we are different than other "managed IT services" company. Gives a brief description of our company and services that can entice clients and potential clients to setup a FREE consultation with us. This will become part of an ongoing marketing campaign that includes emails, leave behinds, brochures, and more

```html
<!DOCTYPE html>
<html lang="en">
<head>
<meta charset="utf-8">
<title>Managed Communications Flyer</title>
<link href="https://fonts.googleapis.com/css2?family=Poppins:wght@300;800&family=Roboto:wght@400;500;700&display=swap" rel="stylesheet">
<style>
  :root {
    --page-bg: #ffffff;
    --sky: #45b5f5;
    --art-light: #3d9ff0;
    --art-deep: #1560d8;
    --navy-left: #2c82c6;
    --navy-mid: #123e86;
    --navy-deep: #050f3a;
    --white: #ffffff;
    --ink: #0a1a3a;
    --tick: #6cc04a;
  }
  * { margin: 0; padding: 0; box-sizing: border-box; }
  html, body { width: 1200px; height: 3384px; overflow: hidden; background: var(--page-bg); }
  .flyer {
    position: absolute; left: 210px; top: 1142px;
    width: 780px; height: 1100px; overflow: hidden;
    background: linear-gradient(135deg, var(--navy-left) 0%, var(--navy-mid) 55%, var(--navy-deep) 100%);
    box-shadow: 0 2px 6px rgba(0,0,0,.25);
    font-family: "Roboto", sans-serif; color: var(--white);
  }
  .network-art {
    position: absolute; left: 0; top: 0; width: 780px; height: 544px;
    background: linear-gradient(160deg, var(--art-light) 0%, var(--art-deep) 100%);
  }
  .headline-panel {
    position: absolute; left: 0; top: 64px; width: 541px; height: 622px;
    background: var(--sky);
    border-radius: 0 300px 290px 0 / 0 330px 290px 0;
  }
  .headline {
    position: absolute; left: 54px; top: 172px;
    font-family: "Poppins", sans-serif; font-size: 57px; line-height: 63px;
    text-transform: uppercase; letter-spacing: -0.5px;
  }
  .headline .light { font-weight: 300; display: block; }
  .headline .strong { font-weight: 800; display: block; }
  .brand-box {
    position: absolute; left: 373px; top: 544px; width: 407px; height: 221px;
    background: var(--white);
    display: flex; align-items: flex-end; justify-content: center; padding-bottom: 26px;
  }
  .brand-name { font-family: "Roboto", sans-serif; font-weight: 700; font-size: 30px; color: var(--ink); }
  .tagline {
    position: absolute; left: 42px; top: 702px;
    font-size: 23px; font-weight: 500; line-height: 33px; text-transform: uppercase;
  }
  .benefits { position: absolute; left: 78px; top: 790px; list-style: none; }
  .benefits li {
    display: flex; align-items: center; gap: 8px;
    font-size: 15px; line-height: 28px; text-transform: uppercase;
  }
  .cta {
    position: absolute; left: 32px; top: 924px; width: 454px; height: 58px;
    background: var(--white); color: var(--ink); border-radius: 29px;
    font-size: 22px; font-weight: 500; display: flex; align-items: center; justify-content: center;
  }
  .contact { position: absolute; left: 57px; top: 1008px; }
  .contact a {
    display: flex; align-items: center; gap: 8px;
    color: var(--white); font-size: 22px; font-weight: 500; line-height: 38px;
    text-decoration: underline;
  }
  .contact a.email { font-size: 19px; }
  .phone {
    position: absolute; left: 462px; top: 1027px;
    display: flex; align-items: center; gap: 10px;
    font-size: 29px; font-weight: 500;
  }
</style>
</head>
<body>
  <main class="flyer">
    <div class="network-art" role="img" aria-label="Isometric illustration of business people among connected servers, devices and a secure data lock"></div>
    <div class="headline-panel"></div>
    <h1 class="headline">
      <span class="light">We're not</span>
      <span class="light">just an IT</span>
      <span class="strong">service</span>
      <span class="strong">provider,</span>
      <span class="light">we're your</span>
      <span class="strong">trusted</span>
      <span class="strong">partner</span>
    </h1>
    <div class="brand-box"><span class="brand-name">Summit Line Networks</span></div>
    <p class="tagline">4 decades of loyalty,<br>uncompromising trust</p>
    <ul class="benefits">
      <li><svg width="16" height="16" viewBox="0 0 16 16"><rect width="16" height="16" rx="2" fill="var(--tick)"/><path d="M3.5 8.5l3 3 6-7" stroke="#fff" stroke-width="2" fill="none"/></svg>Customized strategic roadmap</li>
      <li><svg width="16" height="16" viewBox="0 0 16 16"><rect width="16" height="16" rx="2" fill="var(--tick)"/><path d="M3.5 8.5l3 3 6-7" stroke="#fff" stroke-width="2" fill="none"/></svg>Proactive cyber security</li>
      <li><svg width="16" height="16" viewBox="0 0 16 16"><rect width="16" height="16" rx="2" fill="var(--tick)"/><path d="M3.5 8.5l3 3 6-7" stroke="#fff" stroke-width="2" fill="none"/></svg>Trust in danger: backup &amp; disaster recovery</li>
      <li><svg width="16" height="16" viewBox="0 0 16 16"><rect width="16" height="16" rx="2" fill="var(--tick)"/><path d="M3.5 8.5l3 3 6-7" stroke="#fff" stroke-width="2" fill="none"/></svg>24/7 dedicated support</li>
    </ul>
    <div class="cta">BOOK A FREE CONSULTATION TODAY.</div>
    <div class="contact">
      <a class="web" href="#"><svg width="22" height="22" viewBox="0 0 22 22"><g fill="none" stroke="var(--tick)" stroke-width="1.6"><circle cx="11" cy="11" r="9"/><ellipse cx="11" cy="11" rx="4" ry="9"/><path d="M2 11h18M4 6h14M4 16h14"/></g></svg>WWW.YOURCOMPANY.COM</a>
      <a class="email" href="#"><svg width="22" height="16" viewBox="0 0 22 16"><rect x="1" y="1" width="20" height="14" fill="var(--tick)"/><path d="M1 1l10 8 10-8" stroke="#fff" stroke-width="1.6" fill="none"/></svg>SUPPORT@YOURCOMPANY.COM</a>
    </div>
    <div class="phone"><svg width="30" height="30" viewBox="0 0 24 24"><path fill="var(--tick)" d="M6.6 10.8a15.2 15.2 0 0 0 6.6 6.6l2.2-2.2c.3-.3.7-.4 1-.2 1.1.4 2.3.6 3.6.6.6 0 1 .4 1 1V20c0 .6-.4 1-1 1A17 17 0 0 1 3 4c0-.6.4-1 1-1h3.5c.6 0 1 .4 1 1 0 1.3.2 2.5.6 3.6.1.3 0 .7-.2 1z"/></svg>123-456-7890</div>
  </main>
</body>
</html>
```